Business Consultancy Business Card Design

Business Card design required for Business Analysis and Project Consultancy business based in Scotland.

Company Name - Brevick Advisory

Back - Company Logo

Front Details

Owen Brevick
07642 918 305
owen.brevick@brevickadvisory.com
http://www.brevickadvisory.com

Colours should match the logo colours but I am open to design ideas.

```html
<!DOCTYPE html>
<html lang="en">
<head>
<meta charset="utf-8">
<title>Brevick Advisory – Business Card</title>
<link rel="stylesheet" href="https://fonts.googleapis.com/css2?family=Open+Sans:wght@300;400;600;700&display=swap">
<style>
  :root {
    --brand-green: #6cb33f;
    --brand-blue: #1b9bd7;
    --ink-grey: #5a5a5a;
    --card-white: #f7f7f7;
    --backdrop: #e3e3e3;
    --shadow: rgba(0, 0, 0, 0.18);
  }
  * { box-sizing: border-box; margin: 0; padding: 0; }
  html, body {
    width: 1200px;
    height: 729px;
    overflow: hidden;
    background: var(--backdrop);
    font-family: "Open Sans", Arial, sans-serif;
  }
  .stage {
    position: relative;
    width: 1200px;
    height: 729px;
    display: flex;
    align-items: center;
    justify-content: center;
    gap: 48px;
  }
  .card {
    position: relative;
    width: 504px;
    height: 288px;
    box-shadow: 0 8px 22px var(--shadow);
    overflow: hidden;
  }

  /* Back side */
  .card--back {
    background: var(--brand-green);
    display: flex;
    align-items: center;
    justify-content: center;
  }
  .wordmark {
    display: flex;
    align-items: center;
    gap: 12px;
  }
  .wordmark__dot {
    width: 30px;
    height: 30px;
    border-radius: 50%;
  }
  .wordmark__name {
    font-weight: 300;
    letter-spacing: 0.5px;
    text-transform: uppercase;
  }
  .card--back .wordmark__dot { background: #ffffff; }
  .card--back .wordmark__name { color: #ffffff; font-size: 24px; }

  /* Front side */
  .card--front { background: var(--card-white); }
  .card--front .wordmark {
    position: absolute;
    top: 42px;
    right: 40px;
    gap: 8px;
  }
  .card--front .wordmark__dot { width: 18px; height: 18px; background: var(--brand-blue); }
  .card--front .wordmark__name { color: var(--ink-grey); font-size: 15px; }

  .contact {
    position: absolute;
    left: 36px;
    top: 150px;
  }
  .contact__name {
    color: var(--brand-green);
    font-size: 25px;
    font-weight: 400;
    line-height: 1.1;
    margin-bottom: 10px;
  }
  .contact__surname { font-weight: 700; }
  .contact__list { list-style: none; }
  .contact__item {
    color: var(--ink-grey);
    font-size: 11px;
    line-height: 1.6;
  }
  .contact__label { display: inline-block; width: 18px; }

  .band {
    position: absolute;
    left: 0;
    bottom: 0;
    width: 100%;
    height: 36px;
    display: flex;
  }
  .band__green { flex: 1; background: var(--brand-green); }
  .band__blue {
    width: 150px;
    background: var(--brand-blue);
    display: flex;
    align-items: center;
    padding-left: 14px;
  }
  .band__dot {
    width: 16px;
    height: 16px;
    border-radius: 50%;
    background: #ffffff;
  }
</style>
</head>
<body>
<main class="stage">
  <section class="card card--back" aria-label="Card back">
    <div class="wordmark">
      <span class="wordmark__dot"></span>
      <span class="wordmark__name">Brevick Advisory</span>
    </div>
  </section>

  <section class="card card--front" aria-label="Card front">
    <div class="wordmark">
      <span class="wordmark__dot"></span>
      <span class="wordmark__name">Brevick Advisory</span>
    </div>

    <div class="contact">
      <h1 class="contact__name">Owen <span class="contact__surname">Brevick</span></h1>
      <ul class="contact__list">
        <li class="contact__item"><span class="contact__label">P:</span>07642 918 305</li>
        <li class="contact__item"><span class="contact__label">E:</span>owen.brevick@brevickadvisory.com</li>
        <li class="contact__item"><span class="contact__label">W:</span>http://www.brevickadvisory.com</li>
      </ul>
    </div>

    <div class="band">
      <span class="band__green"></span>
      <span class="band__blue"><span class="band__dot"></span></span>
    </div>
  </section>
</main>
</body>
</html>
```